Institute for Hollow Relief at Annapolis
business card and stationary
Institute for Hollow Relief at Annapolis -
Creative Brief
Professional
Dominic T. Halloway, MD
472 Fenwick Court, Suite 208 Annapolis, MD 21409
dthalloway82@mailbright.example
www.wombrelief.example
Use new logo Comprehensive Gynecologic Care with Specialization in Chronic Pain Disorders and Minimally Invasive Surgery
Appointment Date and Time: Mon. _______ Tue _____ Wed ______ Thurs_______ Fri_______ _______ AM _______ PM

```html
<!DOCTYPE html>
<html lang="en">
<head>
<meta charset="utf-8">
<title>Institute for Hollow Relief at Annapolis — Stationery</title>
<link rel="stylesheet" href="https://fonts.googleapis.com/css2?family=Open+Sans:wght@400;600;700&display=swap">
<style>
:root{
  --board:#5b2e0e;
  --paper:#ffffff;
  --plum:#84507f;
  --plum-dark:#5f2f5c;
  --lilac:#d8c4d8;
  --lilac-soft:#efe5ef;
  --ink:#555555;
  --rule:#9a9a9a;
  --label:#e8d9c8;
}
*{box-sizing:border-box;margin:0;padding:0}
html,body{width:1200px;height:540px;overflow:hidden}
body{background:var(--board);font-family:"Open Sans",Arial,sans-serif;color:var(--ink);position:relative}
.sheet,.envelope,.card{position:absolute;background:var(--paper);overflow:hidden;box-shadow:0 2px 6px rgba(0,0,0,.35)}
.swoosh{position:absolute;left:0;bottom:0;width:100%}
.brand{position:absolute;display:flex;align-items:center;gap:5px}
.brand-dot{width:16px;height:16px;border-radius:50%;background:var(--plum);flex:none}
.brand-name{font-weight:700;color:var(--plum);font-size:7px;line-height:1.15;text-transform:uppercase;letter-spacing:.2px}
.contact{position:absolute;font-size:4.4px;line-height:1.45;color:var(--ink)}
.web{position:absolute;font-size:5px;color:var(--plum);font-weight:600}
.watermark{position:absolute;border-radius:50%;background:radial-gradient(circle,var(--lilac-soft) 0%,rgba(239,229,239,0) 70%)}
.option-label{position:absolute;top:512px;font-size:13px;color:var(--label)}

/* letterhead */
.letterhead{left:43px;top:34px;width:312px;height:466px}
.letterhead .brand{left:18px;top:18px}
.letterhead .contact{left:176px;top:18px}
.letterhead .watermark{left:80px;top:170px;width:200px;height:200px}
.letterhead .web{left:16px;bottom:10px}

/* fax */
.fax{left:380px;top:34px;width:316px;height:466px}
.fax .brand{left:18px;top:18px}
.fax .contact{left:176px;top:18px}
.fax-title{position:absolute;left:18px;top:78px;font-size:17px;font-weight:700;color:#333}
.fax-fields{position:absolute;left:18px;top:108px;width:280px;display:grid;grid-template-columns:1fr 1fr;column-gap:12px;row-gap:9px}
.fax-field{font-size:5px;color:var(--ink);border-bottom:0.7px solid var(--rule);padding-bottom:2px}
.fax-checks{position:absolute;left:18px;top:196px;width:280px;display:flex;justify-content:space-between}
.fax-check{display:flex;align-items:center;gap:3px;font-size:5px}
.fax-check i{display:block;width:6px;height:6px;border:0.7px solid #777}
.fax .watermark{left:130px;top:250px;width:170px;height:170px}
.fax .web{left:16px;bottom:10px}

/* envelopes */
.envelope-back{left:734px;top:34px;width:437px;height:177px}
.envelope-back .flap{position:absolute;left:0;top:0;width:100%;height:100%}
.envelope-front{left:720px;top:140px;width:437px;height:145px}
.envelope-front .brand{left:18px;top:16px}
.envelope-front .contact{left:18px;top:50px}
.envelope-front .web{left:14px;bottom:6px}

/* business cards */
.card{top:365px;width:186px;height:134px}
.card-front{left:720px}
.card-front .person{position:absolute;left:14px;top:10px;font-size:5px;line-height:1.45}
.card-front .person strong{font-size:5.5px;color:#333}
.card-front .brand{left:14px;top:44px}
.card-front .contact{left:14px;top:78px}
.card-front .web{left:12px;bottom:6px}
.card-back{left:917px}
.appt{position:absolute;left:14px;top:14px;right:12px;font-size:4.6px;line-height:1.3}
.appt h3{font-size:6px;color:var(--plum);font-weight:700;margin-bottom:6px;text-align:center}
.appt-row{display:flex;flex-wrap:wrap;gap:4px 8px;margin-bottom:6px}
.appt-row span::after{content:"";display:inline-block;width:18px;border-bottom:0.6px solid var(--rule);margin-left:2px}
.tagline{position:absolute;left:14px;right:12px;bottom:26px;font-size:4.2px;line-height:1.35;color:var(--plum-dark);text-align:center}
</style>
</head>
<body>

<!-- Letterhead -->
<section class="sheet letterhead">
  <div class="brand"><span class="brand-dot"></span><span class="brand-name">Institute for<br>Hollow Relief<br>at Annapolis</span></div>
  <div class="contact">472 Fenwick Court, Suite 208<br>Annapolis, MD 21409<br>P 410.555.0148<br>F 410.555.0179<br>dthalloway82@mailbright.example</div>
  <div class="watermark"></div>
  <svg class="swoosh" viewBox="0 0 312 40" height="40" preserveAspectRatio="none">
    <path d="M0 22 Q150 4 312 14 L312 40 L0 40Z" fill="var(--lilac)"/>
    <path d="M0 30 Q160 12 312 22 L312 28 Q160 20 0 34Z" fill="var(--plum)"/>
  </svg>
  <div class="web">www.wombrelief.example</div>
</section>
<div class="option-label" style="left:204px">Option 1</div>

<!-- Fax -->
<section class="sheet fax">
  <div class="brand"><span class="brand-dot"></span><span class="brand-name">Institute for<br>Hollow Relief<br>at Annapolis</span></div>
  <div class="contact">472 Fenwick Court, Suite 208<br>Annapolis, MD 21409<br>P 410.555.0148<br>F 410.555.0179<br>dthalloway82@mailbright.example</div>
  <div class="fax-title">FAX</div>
  <div class="fax-fields">
    <div class="fax-field">To:</div><div class="fax-field">From:</div>
    <div class="fax-field">Fax:</div><div class="fax-field">Pages:</div>
    <div class="fax-field">Phone:</div><div class="fax-field">Date:</div>
    <div class="fax-field">Re:</div><div class="fax-field">CC:</div>
  </div>
  <div class="fax-checks">
    <span class="fax-check"><i></i>Urgent</span>
    <span class="fax-check"><i></i>For Review</span>
    <span class="fax-check"><i></i>Please Comment</span>
    <span class="fax-check"><i></i>Please Reply</span>
    <span class="fax-check"><i></i>Please Recycle</span>
  </div>
  <div class="watermark"></div>
  <svg class="swoosh" viewBox="0 0 316 40" height="40" preserveAspectRatio="none">
    <path d="M0 22 Q150 4 316 14 L316 40 L0 40Z" fill="var(--lilac)"/>
    <path d="M0 30 Q160 12 316 22 L316 28 Q160 20 0 34Z" fill="var(--plum)"/>
  </svg>
  <div class="web">www.wombrelief.example</div>
</section>
<div class="option-label" style="left:540px">Option 2</div>

<!-- Envelope back -->
<section class="envelope envelope-back">
  <svg class="flap" viewBox="0 0 437 177" preserveAspectRatio="none">
    <path d="M0 0 L218 95 L437 0" fill="none" stroke="#cfcfcf" stroke-width="1"/>
    <path d="M0 0 L437 0 L437 18 Q218 4 0 22Z" fill="var(--lilac)"/>
    <circle cx="218" cy="40" r="26" fill="var(--lilac-soft)"/>
  </svg>
</section>

<!-- Envelope front -->
<section class="envelope envelope-front">
  <div class="brand"><span class="brand-dot"></span><span class="brand-name">Institute for<br>Hollow Relief<br>at Annapolis</span></div>
  <div class="contact">472 Fenwick Court, Suite 208<br>Annapolis, MD 21409</div>
  <svg class="swoosh" viewBox="0 0 437 30" height="30" preserveAspectRatio="none">
    <path d="M0 16 Q220 2 437 10 L437 30 L0 30Z" fill="var(--lilac)"/>
    <path d="M0 22 Q220 8 437 16 L437 21 Q220 14 0 26Z" fill="var(--plum)"/>
  </svg>
  <div class="web">www.wombrelief.example</div>
</section>

<!-- Business card front -->
<section class="card card-front">
  <div class="person"><strong>Dominic T. Halloway, MD</strong><br>Gynecologic Surgery</div>
  <div class="brand"><span class="brand-dot"></span><span class="brand-name">Institute for<br>Hollow Relief<br>at Annapolis</span></div>
  <div class="contact">472 Fenwick Court, Suite 208 Annapolis, MD 21409<br>P 410.555.0148 &nbsp; F 410.555.0179<br>dthalloway82@mailbright.example</div>
  <svg class="swoosh" viewBox="0 0 186 22" height="22" preserveAspectRatio="none">
    <path d="M0 12 Q90 2 186 8 L186 22 L0 22Z" fill="var(--lilac)"/>
    <path d="M0 16 Q90 6 186 12 L186 15 Q90 10 0 19Z" fill="var(--plum)"/>
  </svg>
  <div class="web">www.wombrelief.example</div>
</section>

<!-- Business card back -->
<section class="card card-back">
  <div class="appt">
    <h3>Appointment Date and Time</h3>
    <div class="appt-row"><span>Mon.</span><span>Tue</span><span>Wed</span></div>
    <div class="appt-row"><span>Thurs</span><span>Fri</span></div>
    <div class="appt-row"><span>AM</span><span>PM</span></div>
  </div>
  <div class="tagline">Comprehensive Gynecologic Care with Specialization in Chronic Pain Disorders and Minimally Invasive Surgery</div>
  <svg class="swoosh" viewBox="0 0 186 22" height="22" preserveAspectRatio="none">
    <path d="M0 12 Q90 2 186 8 L186 22 L0 22Z" fill="var(--lilac)"/>
    <path d="M0 16 Q90 6 186 12 L186 15 Q90 10 0 19Z" fill="var(--plum)"/>
  </svg>
</section>

</body>
</html>
```